Halloween Party Invitation

Need a one page flyer for our party Oct 29, 2019

Colors
ef4147
ffffff
fbed22

Requirements
Must have
• Carnival and Scary Clown Theme "Gloomy the Jester presents"
• "till death do us party"
• Tuesday Oct 29, 2019 . 7pm -midnight, kids welcome 7-9
• Open Hosted Bar
• Hair Raising Carnival Food
• Carnival Games
• at the Riverside Ember Hall, 4718 Harlow Creek Ave
• RSVP Requested - Guest list strictly enforced
• Costumes Strongly Suggested
• Haunted House, Dancing and Special Surprise Performance
• Riverside Ember Hall - photo attached but you can make it look like a scary halloween venue.
• The Marlow Kitchens logo attached
Nice to have
• - Big Top Tent as in a carnival or circus.
• Super scary clowns as the hosts and guests
• Very Colorful
• Scary clown faces and one full bodied clown
• Jack o lanterns (scary cared pumpkins)

```html
<!DOCTYPE html>
<html lang="en">
<head>
<meta charset="utf-8">
<title>Halloween Party Flyer</title>
<link rel="stylesheet" href="https://fonts.googleapis.com/css2?family=Oswald:wght@400;500;600;700&family=Pirata+One&family=Creepster&display=swap">
<style>
  :root {
    --stage: #9a9a9a;
    --night: #0b1412;
    --night-blue: #16283a;
    --red: #ef4147;
    --white: #ffffff;
    --yellow: #fbed22;
    --ink: #1a1a1a;
    --gold-light: #f3e3a0;
    --gold-dark: #9a7a2a;
    --wood-light: #8a4f22;
    --wood-dark: #3e1f0c;
    --pumpkin: #f08a1c;
    --pumpkin-deep: #7a2a08;
  }
  * { box-sizing: border-box; margin: 0; padding: 0; }
  html, body { width: 1200px; height: 1200px; overflow: hidden; }
  body { background: var(--stage); position: relative; font-family: "Oswald", sans-serif; }

  .flyer {
    position: absolute; left: 192px; top: 0; width: 815px; height: 1200px;
    overflow: hidden;
  }
  .flyer__backdrop {
    position: absolute; inset: 0;
    background:
      radial-gradient(ellipse 60% 40% at 55% 52%, #1f3a52 0%, rgba(22,40,58,0) 70%),
      radial-gradient(ellipse 70% 50% at 85% 60%, rgba(40,80,120,0.35) 0%, rgba(0,0,0,0) 70%),
      linear-gradient(180deg, #0a1210 0%, var(--night-blue) 55%, var(--night) 100%);
  }
  .presenter {
    position: absolute; top: 62px; width: 100%; text-align: center;
    color: var(--white); font-weight: 600; font-size: 22px; letter-spacing: 0.3px;
  }
  .sign-board {
    position: absolute; left: 87px; top: 103px; width: 635px; height: 240px;
    background: linear-gradient(180deg, var(--wood-light) 0%, #6b3a17 50%, var(--wood-dark) 100%);
    border-radius: 6px;
  }
  .headline {
    position: absolute; left: 0; top: 0; width: 815px; height: 460px;
    overflow: visible;
  }
  .headline__title { font-family: "Pirata One", serif; font-size: 215px; }
  .headline__sub { font-family: "Creepster", cursive; font-size: 130px; }
  .venue {
    position: absolute; top: 446px; width: 100%; text-align: center;
    color: var(--red); font-weight: 600; font-size: 31px; line-height: 1.3;
  }
  .date-band {
    position: absolute; left: 192px; top: 501px; width: 440px; height: 32px;
    background: var(--yellow); color: var(--ink);
    font-weight: 500; font-size: 24px; line-height: 32px; text-align: center;
  }
  .kids-note {
    position: absolute; top: 538px; width: 100%; text-align: center;
    color: var(--white); font-weight: 500; font-size: 22px;
  }
  .lantern-scene {
    position: absolute; left: 127px; top: 581px; width: 507px; height: 308px;
    background: radial-gradient(ellipse 55% 55% at 50% 60%, #ffcc3a 0%, var(--pumpkin) 35%, var(--pumpkin-deep) 75%, rgba(122,42,8,0) 100%);
  }
  .tagline {
    position: absolute; top: 906px; left: 90px; width: 632px; text-align: center;
    color: var(--yellow); font-weight: 600; font-size: 63px; line-height: 1.1; letter-spacing: 0.3px;
    white-space: nowrap;
  }
  .perks { position: absolute; top: 1008px; left: 0; width: 100%; list-style: none; }
  .perks__item {
    position: absolute; display: flex; align-items: center; gap: 6px;
    color: var(--white); font-weight: 500; font-size: 11.5px; white-space: nowrap;
  }
  .perks__item svg { width: 9px; height: 9px; flex: none; }
  .host-mark {
    position: absolute; left: 280px; top: 1083px; width: 254px; height: 75px;
    background: var(--white); display: flex; align-items: center; justify-content: center; gap: 10px;
  }
  .host-mark__square { width: 26px; height: 26px; background: var(--ink); }
  .host-mark__name { color: var(--ink); font-family: "Oswald", sans-serif; font-weight: 500; font-size: 22px; }
</style>
</head>
<body>
  <main class="flyer">
    <div class="flyer__backdrop" role="img" aria-label="Dark haunted venue interior with cobwebs, barbed wire and stacked skulls"></div>

    <p class="presenter">GLOOMY THE JESTER PRESENTS</p>

    <div class="sign-board" role="img" aria-label="Weathered wooden sign hanging from barbed wire"></div>

    <svg class="headline" viewBox="0 0 815 460" aria-label="Halloween Party">
      <defs>
        <linearGradient id="gold" x1="0" y1="0" x2="0" y2="1">
          <stop offset="0" stop-color="#fff4c0"/>
          <stop offset="0.45" stop-color="#f3e3a0"/>
          <stop offset="1" stop-color="#9a7a2a"/>
        </linearGradient>
      </defs>
      <text class="headline__title" x="157" y="295" textLength="526" lengthAdjust="spacingAndGlyphs" fill="url(#gold)">HALLOWEEN</text>
      <text class="headline__sub" x="276" y="425" textLength="301" lengthAdjust="spacingAndGlyphs" fill="#ffffff" transform="rotate(-3 426 370)">PARTY</text>
    </svg>

    <p class="venue">Riverside Ember Hall, 4718 Harlow Creek Ave</p>
    <p class="date-band">Tuesday Oct 29, 2019 . 7pm -midnight</p>
    <p class="kids-note">Kids welcome 7-9</p>

    <div class="lantern-scene" role="img" aria-label="Three glowing carved jack-o'-lanterns with splashes of blood and skulls"></div>

    <h2 class="tagline">TILL DEATH DO US PARTY</h2>

    <ul class="perks">
      <li class="perks__item" style="left:92px;top:0"><svg viewBox="0 0 10 10"><circle cx="5" cy="5" r="5" fill="#ef4147"/><path d="M2.8 5.2l1.5 1.5 2.9-3" stroke="#fff" stroke-width="1.2" fill="none"/></svg>Open Hosted Bar</li>
      <li class="perks__item" style="left:92px;top:19px"><svg viewBox="0 0 10 10"><circle cx="5" cy="5" r="5" fill="#ef4147"/><path d="M2.8 5.2l1.5 1.5 2.9-3" stroke="#fff" stroke-width="1.2" fill="none"/></svg>Hair Raising Carnival Food</li>
      <li class="perks__item" style="left:237px;top:0"><svg viewBox="0 0 10 10"><circle cx="5" cy="5" r="5" fill="#ef4147"/><path d="M2.8 5.2l1.5 1.5 2.9-3" stroke="#fff" stroke-width="1.2" fill="none"/></svg>Carnival Games</li>
      <li class="perks__item" style="left:237px;top:19px"><svg viewBox="0 0 10 10"><circle cx="5" cy="5" r="5" fill="#ef4147"/><path d="M2.8 5.2l1.5 1.5 2.9-3" stroke="#fff" stroke-width="1.2" fill="none"/></svg>RSVP Requested - Guest list strictly enforced</li>
      <li class="perks__item" style="left:471px;top:0"><svg viewBox="0 0 10 10"><circle cx="5" cy="5" r="5" fill="#ef4147"/><path d="M2.8 5.2l1.5 1.5 2.9-3" stroke="#fff" stroke-width="1.2" fill="none"/></svg>Costumes Strongly Suggested</li>
      <li class="perks__item" style="left:471px;top:19px"><svg viewBox="0 0 10 10"><circle cx="5" cy="5" r="5" fill="#ef4147"/><path d="M2.8 5.2l1.5 1.5 2.9-3" stroke="#fff" stroke-width="1.2" fill="none"/></svg>Haunted House, Dancing and Special Surprise Performance</li>
    </ul>

    <div class="host-mark">
      <span class="host-mark__square"></span>
      <span class="host-mark__name">The Marlow Kitchens</span>
    </div>
  </main>
</body>
</html>
```